Iconic website for iconic products

We want a website which will stand out, which will reflect that we are offering cutting edge solutions, breaking the mould. The website must be very search engine friendly, to drive traffic from all around the world, and also sticky, so that they explore what we have to offer, and hopefully buy from us.

We have launched a portfolio of products in the field of 3D, which are highly accessible. They are accessible in their openness, their ease of use and their ultra low cost. We are providing everyone everywhere the opportunity to engage in 3D design and to produce physical 3D models as outputs from their designs. This technology is ground breaking and world changing.

The website will need to be easy for us to maintain and grow, easy for our customers and prospects to use, easy to find.

We will need to integrate a blog, and provide eCommerce capability. We will also be looking to add a forum, which we will need to monitor and maintain, so that our customers can connect with one another, share best practice, offer solutions to problems, and generate value for one another, while reducing our after-sales support burden.

We will also need to set up page templates for our key customers to show what they have done with our products so that others can share the experience.

Target Market(s)

We have a number of distinct markets.
Education:
Primary (5-11) schools
Secondary (11-18) schools
Colleges (16-19)
Universities
Creative designers and designer-makers
Industrial companies; any that are involved in design, in manufacture, in marketing
Animation, games and virtual world organisations
Hobbyists

Industry/Entity Type

Sales

Requirements
Must have
• Iconic design
• Ease of maintenance and future build
• Blog
• eCommerce
• Forum
• Twitter
• When people enquire, people must fill in forms to download information, and we must capture that information on a database.
• We also need a secure log in area for distributors and resellers to access for confidential information.
Nice to have
• An updated logo to match the website
Should not have
• Old fashioned design
• Bricks and mortar feel

```html
<!DOCTYPE html>
<html lang="en">
<head>
<meta charset="utf-8">
<title>Q7 Technologies – Incredibly low cost 3D technologies</title>
<link href="https://fonts.googleapis.com/css2?family=Poppins:wght@500;600&family=Questrial&family=Noto+Sans:wght@400;700&family=Dancing+Script:wght@600&display=swap" rel="stylesheet">
<style>
:root{
  --red:#c1000b;
  --red-dark:#a00008;
  --red-panel:#c7242b;
  --red-text:#a0151c;
  --charcoal:#242424;
  --charcoal-2:#2f2f2f;
  --white:#ffffff;
  --ink:#222222;
  --grey-card:#f6f6f6;
}
*{margin:0;padding:0;box-sizing:border-box}
html,body{width:888px;height:1200px;overflow:hidden}
body{position:relative;background:var(--white);font-family:"Noto Sans",Verdana,sans-serif;color:var(--ink)}
.abs{position:absolute}

.site-header{left:0;top:0;width:888px;height:88px;background:linear-gradient(180deg,#c8000c 0%,#b90009 80%,#9c0007 100%)}
.brand{left:107px;top:26px;font-family:"Poppins",sans-serif;font-weight:600;font-size:25px;color:var(--white);letter-spacing:.2px;display:flex;align-items:center;gap:7px}
.brand-dot{width:9px;height:9px;border-radius:50%;background:var(--white)}
.tagline{left:540px;top:30px;width:240px;font-family:"Dancing Script",cursive;font-size:14px;color:var(--white);line-height:21px}
.tagline .l2{padding-left:52px;display:block}
.tagline b{font-family:"Poppins",sans-serif;font-size:14px}

.hero-band{left:0;top:88px;width:888px;height:221px;background:radial-gradient(ellipse at 30% 40%,#353535 0%,var(--charcoal) 70%);border-bottom:6px solid var(--red)}
.main-nav{left:365px;top:98px;height:30px;display:flex}
.main-nav a{font-family:"Poppins",sans-serif;font-weight:500;font-size:10px;color:var(--white);text-decoration:none;padding:0 15px;line-height:30px;border-left:1px solid #5a5a5a}
.main-nav a:last-child{border-right:1px solid #5a5a5a}

.slider{left:105px;top:127px;width:676px;height:253px;background:var(--red);padding:5px}
.slider-image{width:100%;height:100%;background:linear-gradient(180deg,#3a3a3a 0%,#6d6a64 45%,#8a6e52 70%,#5c4c3e 100%);position:relative}
.slider-caption{left:0;top:65px;width:285px;height:87px;background:rgba(170,10,16,.88);padding:8px 14px;font-family:"Poppins",sans-serif;font-weight:500;font-size:10.6px;line-height:13.4px;color:var(--white)}
.slider-controls{left:0;bottom:0;width:100%;height:23px;background:rgba(60,60,60,.75);display:flex;align-items:center;padding-left:19px;gap:4px}
.slider-controls span{width:13px;height:13px;background:#111;color:var(--white);font-size:7px;font-weight:700;display:flex;align-items:center;justify-content:center}
.slider-controls span.active{background:var(--white);color:#111}
.slider-controls .gap{width:16px;background:none}
.slider-controls .pager{margin-right:8px}

.content{left:110px;top:380px;width:666px;height:792px;background:var(--white);box-shadow:0 0 6px rgba(0,0,0,.25)}

.h-section{font-family:"Questrial",sans-serif;font-weight:400;color:var(--red-text);font-size:18px}
.copy{font-size:8.6px;line-height:12.6px;color:var(--ink);width:380px}
.more-link{font-size:8px;font-weight:700;color:var(--ink);display:flex;align-items:center;gap:4px}
.more-link i{width:8px;height:8px;background:var(--red-text);display:inline-block;clip-path:polygon(0 0,100% 0,100% 100%,0 100%);position:relative}
.more-link i::after{content:"";position:absolute;left:2px;top:1.5px;border-left:4px solid var(--white);border-top:2.5px solid transparent;border-bottom:2.5px solid transparent}

.price{left:436px;top:688px;font-size:8.8px;font-weight:700;color:var(--ink)}
.product-photo{border:1px solid #8a5a2a;background:linear-gradient(135deg,#4a6d8e 0%,#2a3f64 40%,#b08a60 75%,#d7b185 100%)}
.wow-title{font-size:8.8px;font-weight:700}
.wow-list{list-style:none;font-size:8.6px;line-height:16.9px}
.wow-list li::before{content:"»";color:var(--red);font-weight:700;margin-right:5px}

.product-card{left:110px;width:373px;height:78px;background:var(--grey-card);padding:6px 0 0 18px}
.product-card h3{font-family:"Questrial",sans-serif;font-weight:400;color:var(--red-text);font-size:13.4px;margin-bottom:3px}
.product-card .from{font-size:8.6px;font-weight:700;letter-spacing:.3px}
.product-card .desc{font-size:8.6px;margin-bottom:8px}
.product-card .info{font-size:8px;font-weight:700;letter-spacing:.3px}
.card-photo{border:1px solid #222}

.side-panel{background:var(--red-panel);box-shadow:inset 0 0 12px rgba(120,0,0,.5)}
.side-panel h2{font-family:"Poppins",sans-serif;font-weight:500;font-size:16.5px;color:var(--white);text-align:center}
.video-box{left:563px;top:417px;width:187px;height:177px;padding-top:3px}
.video-screen{left:14px;top:31px;width:159px;height:106px;background:linear-gradient(180deg,#3a2d24 0%,#3b33a8 45%,#6a3ec8 60%,#2c2422 100%)}
.play{left:72px;top:44px;border-left:12px solid var(--white);border-top:7px solid transparent;border-bottom:7px solid transparent}
.video-controls{left:14px;top:137px;width:159px;height:21px;background:var(--white);display:flex;align-items:center;padding:0 6px;gap:6px;font-size:5px;color:#444}
.vc-play{border-left:9px solid #333;border-top:5px solid transparent;border-bottom:5px solid transparent}
.vc-track{width:36px;height:4px;border-radius:2px;background:#ddd;position:relative}
.vc-track::before{content:"";position:absolute;left:0;top:-1.5px;width:7px;height:7px;border-radius:50%;background:#444}
.vc-screen{width:9px;height:7px;border:1.5px solid #444}

.enquiry{left:563px;top:615px;width:186px;height:274px;padding:4px 12px 0}
.enquiry label{display:block;font-size:8.4px;font-weight:700;color:var(--white);margin-top:6px;margin-bottom:3px;letter-spacing:.3px}
.enquiry .field{width:161px;height:18px;background:var(--white);border:1px solid #d88}
.enquiry .field.tall{height:70px}
.form-actions{display:flex;gap:7px;margin-top:6px;padding-left:21px}
.btn{width:59px;height:20px;background:linear-gradient(#fafafa,#d9d9d9);border:1px solid #999;font-size:8.6px;font-weight:700;color:#222;display:flex;align-items:center;justify-content:center}

.promo{left:564px;width:186px;height:61px;background:linear-gradient(180deg,#d0000b,#a90008);border-radius:3px;display:flex;align-items:center;padding-left:9px;gap:15px;font-family:"Poppins",sans-serif;font-weight:600;font-size:16px;color:var(--white)}
.promo-reflect{left:564px;width:186px;height:26px;background:linear-gradient(180deg,rgba(180,0,0,.12),rgba(255,255,255,0))}

.site-footer{left:0;top:1172px;width:888px;height:28px;background:var(--red);font-size:7.2px;font-weight:700;color:var(--white)}
.site-footer .left{position:absolute;left:128px;top:10px}
.site-footer .right{position:absolute;left:633px;top:10px}
</style>
</head>
<body>

<header class="abs site-header"></header>
<div class="abs brand"><span class="brand-dot"></span>Q7 Technologies</div>
<p class="abs tagline">Incredibly low cost <b>3D</b> technologies<span class="l2">for designing and producing 3d models</span></p>

<div class="abs hero-band"></div>
<nav class="abs main-nav">
  <a href="#">Home</a><a href="#">Product</a><a href="#">Gallery</a><a href="#">News</a><a href="#">Contact</a><a href="#">Order</a><a href="#">Forum</a>
</nav>

<section class="abs slider">
  <div class="slider-image" role="img" aria-label="Close-up photo of a desktop 3D printer building a translucent model on a wooden platform">
    <p class="abs slider-caption">Q7 Technologies offers schools and colleges cutting edge products and solutions in the fields of 3D modelling and printing, at incredibly low prices. Ideal for teaching and learning.</p>
    <div class="abs slider-controls">
      <span>&#8249;</span><span class="pager">&#8250;</span><span class="gap"></span>
      <span>1</span><span class="active">2</span><span>3</span><span>4</span><span>5</span>
    </div>
  </div>
</section>

<main class="abs content"></main>

<h1 class="abs h-section" style="left:128px;top:414px">Welcome to Q7 Technologies</h1>
<p class="abs copy" style="left:128px;top:447px">Lorem Ipsum is simply dummy text of the printing and typesetting industry. Lorem Ipsum has been the industry's standard dummy text ever since the 1500s, when an unknown printer took a galley of type and scrambled it to make a type specimen book.</p>
<p class="abs copy" style="left:128px;top:510px;width:385px">It has survived not only five centuries, but also the leap into electronic typesetting, remaining essentially unchanged. It was popularised in the 1960s with the release of Lettersheet sheets containing Lorem Ipsum passages, and more recently with desktop publishing software like PageForge including versions of Lorem Ipsum.</p>
<a class="abs more-link" style="left:128px;top:569px"><i></i>Read More</a>

<h2 class="abs h-section" style="left:128px;top:610px">Our Products Range</h2>
<p class="abs copy" style="left:128px;top:641px">below are our full range of products..</p>

<h2 class="abs h-section" style="left:128px;top:677px">MORPHEO 3D creative solution</h2>
<p class="abs price">PRICE: £ 495.00</p>
<p class="abs copy" style="left:128px;top:710px;width:225px">The easy way to design creative 3D models on a PC without having to learn or use 3D CAD.</p>
<p class="abs copy" style="left:128px;top:748px;width:225px">Morpheo is a cutting edge ‘haptic’ technology which delivers a high quality, immersive 3D ....</p>
<div class="abs product-photo" style="left:369px;top:711px;width:138px;height:102px" role="img" aria-label="Photo of a laptop showing a 3D model beside a haptic pen controller"></div>
<p class="abs wow-title" style="left:128px;top:798px">Morpheo’s WOW factors:</p>
<ul class="abs wow-list" style="left:128px;top:812px">
  <li>Use our 3D mouse to 'touch' and feel the 3 dimensional qualities of a virtual object</li>
  <li>Movement in all directions to manipulate and construct objects within a 3D space</li>
  <li>Sense of touching and moving freely, tapping into your natural way of doing things</li>
  <li>Feel where you are, whether inside or outside objects</li>
  <li>So easy to create organic shapes</li>
  <li>Change the hardness/softness of virtual objects for different effects</li>
  <li>Straightforward interface for a more intuitive way to sketch and model</li>
</ul>
<a class="abs more-link" style="left:128px;top:943px"><i></i>&nbsp;Other Products</a>

<article class="abs product-card" style="top:971px">
  <h3>Morpheo 3D creative</h3>
  <p class="from">package from £350</p>
  <p class="desc">for designing creative 3D models</p>
  <p class="info">Click for more information</p>
</article>
<div class="abs card-photo" style="left:370px;top:974px;width:92px;height:73px;background:radial-gradient(ellipse at 45% 45%,#cfe0e6 0%,#7fa4c4 35%,#2c3a8a 75%)" role="img" aria-label="Photo of a printed spiral 3D sculpture on a blue background"></div>

<article class="abs product-card" style="top:1064px">
  <h3>Trace 3D Laserscanner</h3>
  <p class="from">from £320</p>
  <p class="desc">for creating virtual 3D models from real objects</p>
  <p class="info">Click for more information</p>
</article>
<div class="abs card-photo" style="left:370px;top:1066px;width:92px;height:73px;background:linear-gradient(180deg,#f4efe8 0%,#c9a27a 55%,#a77c52 100%)" role="img" aria-label="Photo of three scanned figurine models on stands"></div>

<aside class="abs side-panel video-box">
  <h2>Video Section</h2>
  <div class="abs video-screen" role="img" aria-label="Video still of a desktop 3D printer lit in blue"></div>
  <div class="abs play"></div>
  <div class="abs video-controls"><span class="vc-play"></span><span>00:00</span><span class="vc-track"></span><span class="vc-screen"></span><span>&#128264;</span><span>buy now</span></div>
</aside>

<aside class="abs side-panel enquiry">
  <h2>Enquiry Now</h2>
  <label>Name</label><div class="field"></div>
  <label style="margin-top:13px">E-mail</label><div class="field"></div>
  <label style="margin-top:13px">Subject</label><div class="field"></div>
  <label style="margin-top:13px">Comments</label><div class="field tall"></div>
  <div class="form-actions"><span class="btn">Submit</span><span class="btn">Clear</span></div>
</aside>

<a class="abs promo" style="top:922px">
  <svg width="47" height="47" viewBox="0 0 47 47" aria-hidden="true">
    <rect x="1" y="1" width="45" height="45" rx="8" fill="#f39a2e" stroke="#c66a10"/>
    <circle cx="12" cy="35" r="5" fill="#fff"/>
    <path d="M8 21a18 18 0 0 1 18 18" stroke="#fff" stroke-width="6" fill="none"/>
    <path d="M8 10a29 29 0 0 1 29 29" stroke="#fff" stroke-width="6" fill="none"/>
  </svg>OUR BLOG</a>
<div class="abs promo-reflect" style="top:984px"></div>

<a class="abs promo" style="top:1031px;gap:10px">
  <svg width="52" height="42" viewBox="0 0 52 42" aria-hidden="true">
    <ellipse cx="19" cy="15" rx="17" ry="12" fill="#f39a2e"/>
    <path d="M9 24 L5 33 L17 26Z" fill="#f39a2e"/>
    <ellipse cx="33" cy="25" rx="16" ry="11" fill="#3a8fd8" stroke="#fff" stroke-width="1.5"/>
    <path d="M40 34 L46 41 L35 35Z" fill="#3a8fd8"/>
  </svg>OUR FORUM</a>
<div class="abs promo-reflect" style="top:1093px"></div>

<footer class="abs site-footer">
  <span class="left">Copyright© Q7 Technologies Ltd 2009-2010 &nbsp;| &nbsp;All Rights Reserved.</span>
  <span class="right">Contact Us | Privacy | Sitemap</span>
</footer>

</body>
</html>
```